Typing Service Business Card Design

Need a new business card design for new logo update. The Keyline Crew is an outsourced typing service. We type audio / voice files into word documents. We are a professional service that is recognised in the industry over the past 15 years and have a strong connection to our brand. The final design should be professional, simple, yet effective.

Business

Contact Information for Business Card

Rosalind Varga
Director

rosalind@kbq.com.au
www.thekeylinecrewbase.com.au

```html
<!DOCTYPE html>
<html lang="en">
<head>
<meta charset="utf-8">
<title>The Keyline Crew – Business Card</title>
<link href="https://fonts.googleapis.com/css2?family=Tinos&display=swap" rel="stylesheet">
<style>
  :root {
    --ink: #000000;
    --paper: #ffffff;
    --magenta: #e02ad0;
    --rose: #d24a9c;
    --backdrop: #e9e7e4;
  }
  * { margin: 0; padding: 0; box-sizing: border-box; }
  html, body {
    width: 1189px; height: 1200px; overflow: hidden;
    background: var(--backdrop);
  }
  .card {
    position: absolute; left: 140px;
    width: 917px; height: 523px;
    background: var(--paper);
    overflow: hidden;
  }
  .card--front { top: 46px; }
  .card--back { top: 623px; }

  .front-art { position: absolute; inset: 0; }

  .brand-name {
    position: absolute;
    font-family: "Tinos", serif;
    font-weight: 400;
    color: var(--paper);
    white-space: nowrap;
    text-align: center;
    line-height: 1;
  }
  .card--front .brand-name { left: 0; width: 480px; top: 238px; font-size: 44px; }

  .person {
    position: absolute; right: 28px; top: 112px;
    text-align: right;
    font-family: "Tinos", serif;
    color: var(--ink);
  }
  .person-name { font-size: 37px; line-height: 1.1; }
  .person-role { font-size: 23px; margin-top: 12px; }

  .contact {
    position: absolute; right: 18px; top: 397px;
    list-style: none;
    font-family: "Tinos", serif;
    font-size: 22px;
    color: var(--ink);
  }
  .contact-item {
    display: flex; align-items: center; justify-content: flex-end;
    gap: 14px; height: 40px;
  }
  .contact-icon { width: 20px; height: 20px; flex: none; }

  .back-band {
    position: absolute; left: 0; right: 0; top: 35px; height: 362px;
    background: var(--ink);
    border-top: 9px solid var(--rose);
    border-bottom: 10px solid var(--rose);
  }
  .card--back .brand-name { left: 0; width: 100%; top: 190px; font-size: 50px; }
</style>
</head>
<body>

<section class="card card--front">
  <svg class="front-art" width="917" height="523" viewBox="0 0 917 523" aria-hidden="true">
    <polygon points="0,0 406,0 563,260 406,523 0,523" fill="var(--ink)"/>
    <polyline points="406,-4 563,260 406,527" fill="none" stroke="var(--magenta)" stroke-width="7"/>
    <line x1="563" y1="260" x2="917" y2="260" stroke="var(--magenta)" stroke-width="6"/>
  </svg>
  <div class="brand-name">The Keyline Crew</div>

  <div class="person">
    <div class="person-name">Rosalind Varga</div>
    <div class="person-role">Director</div>
  </div>

  <ul class="contact">
    <li class="contact-item">
      <span>rosalind@kbq.com.au</span>
      <svg class="contact-icon" viewBox="0 0 20 20" aria-hidden="true">
        <rect width="20" height="20" fill="var(--magenta)"/>
        <rect x="4" y="6" width="12" height="8" fill="none" stroke="var(--paper)" stroke-width="1.4"/>
        <polyline points="4,6 10,11 16,6" fill="none" stroke="var(--paper)" stroke-width="1.4"/>
      </svg>
    </li>
    <li class="contact-item">
      <span>www.thekeylinecrewbase.com.au</span>
      <svg class="contact-icon" viewBox="0 0 20 20" aria-hidden="true">
        <rect width="20" height="20" fill="var(--magenta)"/>
        <circle cx="10" cy="10" r="5.5" fill="none" stroke="var(--paper)" stroke-width="1.3"/>
        <ellipse cx="10" cy="10" rx="2.3" ry="5.5" fill="none" stroke="var(--paper)" stroke-width="1.1"/>
        <line x1="4.5" y1="10" x2="15.5" y2="10" stroke="var(--paper)" stroke-width="1.1"/>
      </svg>
    </li>
  </ul>
</section>

<section class="card card--back">
  <div class="back-band"></div>
  <div class="brand-name">The Keyline Crew</div>
</section>

</body>
</html>
```